KTMR Social Media Layouts

Our client needs a social media layouts for a personal injury law firm based in Baltimore, Maryland. We've attached the logo we recently had created (but is not in use). The law firm is undergoing a complete rebrand. We would like to see options facebook layouts, but they will also be needing image sizes for linkedin, twitter and instagram.

```html
<!DOCTYPE html>
<html lang="en">
<head>
<meta charset="UTF-8">
<title>KTMR Law – Cover Banner</title>
<link rel="stylesheet" href="https://fonts.googleapis.com/css2?family=Libre+Baskerville:wght@400;700&display=swap">
<style>
  :root {
    --stage-grey: #8c8c8c;
    --navy: #10133a;
    --paper: #ffffff;
    --mist-top: #f4f5f0;
    --mist-mid: #e6e8e3;
    --water: #d4d6d2;
  }
  * { box-sizing: border-box; margin: 0; padding: 0; }
  html, body {
    width: 1200px;
    height: 1200px;
    overflow: hidden;
    background: var(--stage-grey);
  }
  .cover {
    position: absolute;
    left: 0;
    top: 378px;
    width: 1200px;
    height: 444px;
    background: var(--navy);
  }
  .cover__band-top { height: 10px; background: var(--navy); }
  .cover__scene {
    position: relative;
    height: 376px;
    overflow: hidden;
  }
  .cover__photo {
    position: absolute;
    inset: 0;
    background: linear-gradient(to bottom,
      var(--mist-top) 0%,
      var(--mist-mid) 68%,
      #c9ccc9 78%,
      var(--water) 82%,
      #e2e3df 100%);
  }
  .brand {
    position: absolute;
    left: 0;
    right: 0;
    top: 44px;
    text-align: center;
    color: var(--navy);
    font-family: "Libre Baskerville", Georgia, serif;
  }
  .brand__mark {
    display: inline-flex;
    align-items: center;
    gap: 26px;
    font-size: 104px;
    font-weight: 400;
    letter-spacing: 0.08em;
    line-height: 1;
  }
  .brand__square {
    width: 70px;
    height: 70px;
    background: var(--navy);
  }
  .brand__partners {
    margin-top: 30px;
    font-size: 23px;
    font-weight: 400;
    letter-spacing: 0.05em;
  }
  .cover__band-mid { height: 15px; background: var(--navy); }
  .cover__tagline {
    height: 29px;
    background: var(--paper);
    color: var(--navy);
    font-family: "Libre Baskerville", Georgia, serif;
    font-weight: 700;
    font-size: 18px;
    letter-spacing: 0.12em;
    text-align: center;
    line-height: 29px;
  }
  .cover__band-bottom { height: 14px; background: var(--navy); }
</style>
</head>
<body>
  <section class="cover">
    <div class="cover__band-top"></div>
    <div class="cover__scene">
      <div class="cover__photo" role="img" aria-label="Misty photograph of a long steel truss bridge stretching across a calm harbour"></div>
      <div class="brand">
        <div class="brand__mark"><span class="brand__square"></span><span>KTMR LAW</span></div>
        <p class="brand__partners">KESSLER, TANNER, MORROW, &amp; REYES, P.A.</p>
      </div>
    </div>
    <div class="cover__band-mid"></div>
    <div class="cover__tagline">PERSONAL INJURY LAW FIRM BASED IN BALTIMORE, MARYLAND</div>
    <div class="cover__band-bottom"></div>
  </section>
</body>
</html>
```